Wine labels Velmora Wine Council - Nueva etiqueta El Consejo Regulador de vinos de Albarrán

Velmora Wines Council, based in southern Spain, are looking to create a new suite of wine labels which retain the elegance of the Velmora Wines industry while reinvigorating their image to the modern era and a new generation of Sherry Wine lovers. These labels will be used across the Velmora Wines Council's range of wines for the promotion of the Velmora Wines industry.

Your design must present at least two styles of Velmora Wines which demonstrate an elegant, modern interpretation and understanding of the unique mood and personality for these wines and the essence of southern Spain.

10 labels will be created based on the winning design, one for each of the unique varieties of Velmora Wines within the collection. This collection comprises of several different wine varieties including: Fino, Manzanilla, Amontillado, Oloroso, Palo Cortado, Medium, Cream, Pale Cream, Pedro Ximenez and Moscatel.

We recommend you visit our website www.velmora-vinos.example/wines as the source to understanding the origins and unique personality of these diverse wines.

El Consejo Regulador de los Vinos de Albarrán y Tordesal quiere renovar las etiquetas de los vinos utilizados para sus actividades de promoción genérica. Esta colección de vinos comprende las tipologías más importantes de la región que incluye: fino, manzanilla, amontillado, oloroso, palo cortado, pale cream, medium, cream, pedro ximénez y moscatel. Por lo tanto se precisan 10 etiquetas, una para cada uno de los vinos mencionados.
Updates

Project Deadline Extended
Reason: Due to some confusion with the deadline we wish to officially extend the deadline to allow designers one last week to submit their entries.

Target Market(s)

Industry, journalists, media, sommeliers, chefs, wine writers

Industry/Entity Type

Council

Requirements
Must have
• Front and Back label plus capsule:
• Front label can have either of the two official logos of the Velmora Wine council titled Vinos de Albarrán Digital or not, this is optional. Must include: Vino selecionado por el Consejo Regulador de la Denominacion de Origen, Name of the variety of wine eg FINO, percentage of alcohol eg 15% and quantity 75 cl.
• The back of the label must include the council logo titled Sellora and 4 additional logos positioned smaller. The Europa logo must appear larger than the 3 other logos. Space for descriptive text about the wine is also required.
• The dimensions of the bottle can be found at this link http://www.vidrialto.example/es/catalogo/vinos-y-espumosos/bordelesas/bd-orla
• Altura:305 mm
• Diámetro base:76,20 mm
• Diámetro hombro:82 mm
• Tipo boca:Cetie
• Peso:750 gr
• Capacidad:75 cl
• Etiqueta delantera y trasera y capsula
• La etiqueta delantera puede incluir el logo oficial del Consejo Regulador o el logo digital, o ninguno, esto es opcional. Debe incluir el siguiete texto: Vino selecionado por el Consejo Regulador de la Denominacion de Origen, el nombre de la variedad del vino, por ejemplo Fino, el porcentaje de alcohol, por ejemplo 15%, y la capacidad 75cl.
• La etiqueta trasera debe incluir el logo oficial Sellora del Consejo, y cuatro logos adicionales con una dimension menor. El Logo de ¨Europa invierte en las zonas rurales¨ debe ser de mayor tamaño que los otros. Se precisa espacio para el texto descriptivo de los vinos.
• Las dimensiones de la botella se puede encontrar en este enlace
• http://www.vidrialto.example/es/catalogo/vinos-y-espumosos/bordelesas/bd-orla
• Altura:305 mm
• Diámetro base:76,20 mm
• Diámetro hombro:82 mm
• Tipo boca:Cetie
• Peso:750 gr
• Capacidad:75 cl
Nice to have
• See our website velmora-vinos.example to understand the origin of the wines. Ver nuestra página web velmora-vinos.example para mejor entender los vinos.
Should not have
• Images of catavinos or stereotypical images from Spain such as flamenco dancers or guitars.

```html
<!DOCTYPE html>
<html lang="es">
<head>
<meta charset="utf-8">
<title>Velmora Wines – Etiquetas</title>
<link href="https://fonts.googleapis.com/css2?family=Cormorant+Garamond:wght@400;500&family=Old+Standard+TT:wght@400&family=Arimo:wght@400;700&display=swap" rel="stylesheet">
<style>
  :root{
    --sky:#f3f2ee;
    --stone:#b09558;
    --stone-dark:#7d6a3a;
    --grass:#4a6330;
    --black:#050505;
    --amber:#7a3a0e;
    --amber-edge:#3c1c07;
    --amber-ink:#7a4418;
    --gold:#f4d548;
    --gold-ink:#e4c03c;
    --sand:#b9b3a2;
    --cream-band:#f5e27b;
    --sand-edge:#cdc6b1;
    --paper:#bfb9a8;
    --ink:#111;
    --white:#f4f1ea;
  }
  *{box-sizing:border-box;margin:0;padding:0}
  html,body{width:1200px;height:889px;overflow:hidden;background:var(--sky)}
  .canvas{position:relative;width:1200px;height:889px;overflow:hidden}
  .backdrop{position:absolute;inset:0;
    background:linear-gradient(180deg,var(--sky) 0%,#ecebe4 8%,#c9b27a 22%,var(--stone) 38%,var(--stone-dark) 58%,#6b6a3c 78%,var(--grass) 100%)}
  .label{position:absolute;box-shadow:6px 8px 18px rgba(0,0,0,.45)}
  .front{top:417px;width:276px;height:429px;overflow:hidden}
  .front--amontillado{left:65px}
  .front--fino{left:474px}
  .front--manzanilla{left:885px}
  .front__head{position:absolute;left:0;top:0;width:100%;height:223px}
  .front--amontillado .front__head,.front--fino .front__head{background:var(--black)}
  .front--manzanilla .front__head{background:var(--sand)}
  .brand{position:absolute;left:0;width:100%;text-align:center}
  .brand__dot{display:block;margin:0 auto 24px;width:14px;height:14px;border-radius:50%;border:1.5px solid currentColor}
  .brand__name{font-family:"Cormorant Garamond",serif;font-weight:400;font-size:14px;letter-spacing:.5px;white-space:nowrap}
  .front .brand{top:62px}
  .front--amontillado .brand{color:var(--amber-ink)}
  .front--fino .brand{color:var(--gold-ink)}
  .front--manzanilla .brand{color:#1d1d1b}
  .scene{position:absolute;left:0;width:100%}
  .front .scene{top:223px;bottom:0}
  .scene--town{background:linear-gradient(180deg,#dfe3e6 0%,#cfd2cf 30%,#b98a70 55%,#a5543c 80%,#6d4535 100%)}
  .scene--castle{background:linear-gradient(180deg,#c9cfd3 0%,#aeb4b6 30%,#8b8a6c 50%,#3f4d2c 75%,#2b3a22 100%)}
  .scene--sunset{background:linear-gradient(180deg,#c9793a 0%,#d8893f 30%,#b9592a 55%,#7e3a1d 85%,#4a2a1a 100%)}
  .scene--hill{background:linear-gradient(180deg,#8a9098 0%,#6f7680 35%,#3c4a34 70%,#1f2b1b 100%)}
  .ribbon{position:absolute;left:0;top:192px;width:276px;height:62px}
  .variety{position:absolute;left:0;top:192px;width:276px;height:52px;line-height:52px;text-align:center;
    font-family:"Old Standard TT",serif;font-size:21px;letter-spacing:1px}
  .front--amontillado .variety{color:#1a0b03}
  .front--fino .variety,.front--manzanilla .variety{color:#0d0d0d}
  .legal{position:absolute;left:0;top:251px;width:100%;text-align:center;font-family:Arimo,sans-serif;font-size:4px;letter-spacing:.1px}
  .legal b{font-weight:700}
  .front--amontillado .legal,.front--fino .legal{color:#e9e4d8}
  .front--manzanilla .legal{color:#2a2a2a}
  .measure{position:absolute;left:8px;right:8px;bottom:8px;display:flex;align-items:center;gap:6px;
    font-family:"Old Standard TT",serif;font-size:10px;color:var(--white)}
  .measure__rule{flex:1;height:1px;background:rgba(255,255,255,.6)}
  .back{top:505px;width:158px;height:286px;overflow:hidden}
  .back--hill{left:316px;background:var(--black)}
  .back--sunset{left:750px;background:var(--paper)}
  .back .scene{top:0;height:135px}
  .back .brand{top:22px;color:var(--gold-ink)}
  .back .brand__dot{margin-bottom:50px}
  .back .brand__name{font-size:13px}
  .back__copy{position:absolute;left:14px;right:14px;top:146px;font-family:Arimo,sans-serif;font-size:4.2px;line-height:5.3px;text-align:justify}
  .back__copy p+p{margin-top:5px}
  .back--hill .back__copy{color:#e8e6e0}
  .back--sunset .back__copy{color:#1b1b1b}
  .seals{position:absolute;left:0;right:0;bottom:10px;display:flex;justify-content:center;align-items:center;gap:14px}
  .seal{display:block}
  .seal--ring{width:14px;height:14px;border-radius:50%}
  .seal--euro{width:26px;height:20px}
  .seal--arch{width:16px;height:12px;border-radius:8px 8px 0 0}
  .back--hill .seal--ring{border:1px solid #ddd}
  .back--hill .seal--euro{background:#f1c400}
  .back--hill .seal--arch{border:1.5px solid #ddd;border-bottom:0}
  .back--sunset .seal--ring{border:1px solid #555}
  .back--sunset .seal--euro{background:#1b2a66}
  .back--sunset .seal--arch{border:1.5px solid #333;border-bottom:0}
</style>
</head>
<body>
<main class="canvas">
  <div class="backdrop" role="img" aria-label="Painted view of a baroque church façade with pinnacles and a long stone balustrade, green grass below"></div>

  <section class="label front front--amontillado">
    <div class="front__head"></div>
    <div class="brand"><span class="brand__dot"></span><span class="brand__name">VELMORA WINES</span></div>
    <div class="scene scene--town" role="img" aria-label="Watercolour of a whitewashed hill town with terracotta roofs and a church tower"></div>
    <svg class="ribbon" viewBox="0 0 276 62" aria-hidden="true">
      <path d="M22 6 H254 Q262 6 262 14 V40 Q262 58 244 58 H32 Q14 58 14 40 V14 Q14 6 22 6 Z" fill="var(--amber-edge)"/>
      <rect x="38" y="3" width="200" height="46" rx="9" fill="var(--amber)"/>
    </svg>
    <div class="variety">AMONTILLADO</div>
    <p class="legal">Wine seleccionado by the <b>REGULATORY COUNCIL</b> of the designation of origin</p>
    <div class="measure"><span>15% alc</span><span class="measure__rule"></span><span>75 cl</span></div>
  </section>

  <section class="label back back--hill">
    <div class="scene scene--hill" role="img" aria-label="Watercolour of a hilltop castle among dark trees under a cloudy sky"></div>
    <div class="brand"><span class="brand__dot"></span><span class="brand__name">VELMORA WINES</span></div>
    <div class="back__copy">
      <p>Lorem ipsum dolor sit amet, consectetuer adipiscing elit. Donec nonummy lacinia leo. Etiam pede nunc, vestibulum vel, rutrum et, tincidunt eu, enim. Morbi turpis arcu, egestas congue, condimentum quis, tristique cursus, leo. Nullam facilisi. Nam portu massa turpis, nonummy et, consectetuer.</p>
      <p>Pellentesque tempor. Mauris tempus diam. Nulla facilisi. Nam sed nisl nec elit suscipit ullamcorper. Nam malesuada sapien eu nibh. Vestibulum viverra varius enim. Nullam venenatis gravida orci. Mauris tincidunt aliquam ante. Phasellus auctor enim eget sem.</p>
      <p>Nulla sed lacus. Curabitur nunc ante, ullamcorper vel, auctor a, aliquam at, tortor. Mauris urna sem, suscipit vitae, dignissim id, ultrices sed, nunc. Pellentesque suscipit accumsan massa. Praesent a lacus vitae turpis consequat semper. Proin semper, neque vel condimentum hendrerit, lectus elit pretium ligula, nec consequat nisl velit at dui.</p>
    </div>
    <div class="seals"><span class="seal seal--ring"></span><span class="seal seal--euro"></span><span class="seal seal--arch"></span></div>
  </section>

  <section class="label front front--fino">
    <div class="front__head"></div>
    <div class="brand"><span class="brand__dot"></span><span class="brand__name">VELMORA WINES</span></div>
    <div class="scene scene--castle" role="img" aria-label="Watercolour of a stone fortress and bell tower on a wooded hill"></div>
    <svg class="ribbon" viewBox="0 0 276 62" aria-hidden="true">
      <path d="M22 6 H254 Q262 6 262 14 V40 Q262 58 244 58 H32 Q14 58 14 40 V14 Q14 6 22 6 Z" fill="var(--black)"/>
      <rect x="38" y="3" width="200" height="46" rx="9" fill="var(--gold)"/>
    </svg>
    <div class="variety">FINO</div>
    <p class="legal">Wine seleccionado by the <b>REGULATORY COUNCIL</b> of the designation of origin</p>
    <div class="measure"><span>15% alc</span><span class="measure__rule"></span><span>75 cl</span></div>
  </section>

  <section class="label back back--sunset">
    <div class="scene scene--sunset" role="img" aria-label="Watercolour of a domed cathedral glowing in warm sunset light"></div>
    <div class="brand"><span class="brand__dot"></span><span class="brand__name">VELMORA WINES</span></div>
    <div class="back__copy">
      <p>Lorem ipsum dolor sit amet, consectetuer adipiscing elit. Donec nonummy lacinia leo. Etiam pede nunc, vestibulum vel, rutrum et, tincidunt eu, enim. Morbi turpis arcu, egestas congue, condimentum quis, tristique cursus, leo. Nullam facilisi. Nam massa turpis, nonummy et, consectetuer.</p>
      <p>Pellentesque tempor. Mauris tempus diam. Nulla facilisi. Nam sed nisl nec elit suscipit ullamcorper. Nam malesuada sapien eu nibh. Vestibulum viverra varius enim. Nullam venenatis gravida orci. Mauris tincidunt aliquam ante. Phasellus auctor enim eget sem.</p>
      <p>Nulla sed lacus. Curabitur nunc ante, ullamcorper vel, auctor a, aliquam at, tortor. Mauris urna sem, suscipit vitae, dignissim id, ultrices sed, nunc. Pellentesque suscipit accumsan massa. Praesent a lacus vitae turpis consequat semper. Proin semper, neque vel condimentum hendrerit, lectus elit pretium ligula, nec consequat nisl velit at dui.</p>
    </div>
    <div class="seals"><span class="seal seal--ring"></span><span class="seal seal--euro"></span><span class="seal seal--arch"></span></div>
  </section>

  <section class="label front front--manzanilla">
    <div class="front__head"></div>
    <div class="brand"><span class="brand__dot"></span><span class="brand__name">VELMORA WINES</span></div>
    <div class="scene scene--sunset" role="img" aria-label="Watercolour of a domed cathedral above rooftops in orange evening light"></div>
    <svg class="ribbon" viewBox="0 0 276 62" aria-hidden="true">
      <path d="M22 6 H254 Q262 6 262 14 V40 Q262 58 244 58 H32 Q14 58 14 40 V14 Q14 6 22 6 Z" fill="var(--sand-edge)"/>
      <rect x="38" y="3" width="200" height="46" rx="9" fill="var(--cream-band)"/>
    </svg>
    <div class="variety">MANZANILLA</div>
    <p class="legal">Wine seleccionado by the <b>REGULATORY COUNCIL</b> of the designation of origin</p>
    <div class="measure"><span>15% alc</span><span class="measure__rule"></span><span>75 cl</span></div>
  </section>
</main>
</body>
</html>
```